High end Electrical/home automation Business Card

Need a card for a high end electrical and home automation company utilising the existing logo.
Phone
Email
Website

Like black look with raised detail. Don’t necessarily need to keep colour of logo it could be made grayscale or white etc

Target Market(s)

High end clients

Contact Information for Business Card

Ridgeline Electrical

Requirements
Must have
• Logo, phone, email, website, address

High end look
Nice to have
• Black background card
Raised font
Should not have
• Lots of colour

```html
<!DOCTYPE html>
<html lang="en">
<head>
<meta charset="utf-8">
<title>Ridgeline Electrical – Business Card</title>
<link rel="stylesheet" href="https://fonts.googleapis.com/css2?family=Roboto:wght@400;500;700&display=swap">
<style>
  :root {
    --backdrop: #8d8d8d;
    --card-black: #1e1e1e;
    --emboss-face: #222222;
    --emboss-light: rgba(255, 255, 255, 0.10);
    --emboss-dark: rgba(0, 0, 0, 0.75);
    --card-white: #ffffff;
    --ink-dark: #2b2b2b;
    --ink-grey: #4a4a4a;
    --ink-light: #f2f2f2;
    --accent: #2a8fd6;
  }
  * { box-sizing: border-box; margin: 0; padding: 0; }
  html, body {
    width: 1200px;
    height: 1043px;
    overflow: hidden;
    background: var(--backdrop);
    font-family: "Roboto", Arial, sans-serif;
  }
  .sheet {
    width: 1200px;
    height: 1043px;
    display: flex;
    flex-direction: column;
    align-items: center;
    justify-content: center;
    gap: 60px;
  }
  .card {
    position: relative;
    width: 760px;
    height: 434px;
    overflow: hidden;
    box-shadow: 0 14px 30px rgba(0, 0, 0, 0.35);
  }
  .card--front { background: var(--card-black); }
  .card--back { background: var(--card-white); }

  /* raised blind-emboss disc on the black side */
  .emboss-disc {
    position: absolute;
    left: 80px;
    top: 50px;
    width: 330px;
    height: 330px;
    border-radius: 50%;
    background: var(--emboss-face);
    box-shadow:
      -2px -2px 1px var(--emboss-light),
      3px 4px 6px var(--emboss-dark),
      inset 1px 1px 1px var(--emboss-light),
      inset -2px -2px 3px var(--emboss-dark);
  }

  .wordmark {
    position: absolute;
    display: flex;
    align-items: center;
    gap: 12px;
    font-weight: 700;
    letter-spacing: -0.5px;
    white-space: nowrap;
  }
  .wordmark__dot {
    width: 14px;
    height: 14px;
    border-radius: 50%;
  }
  .card--front .wordmark {
    right: 50px;
    top: 250px;
    font-size: 44px;
    color: var(--ink-light);
  }
  .card--back .wordmark {
    right: 60px;
    top: 110px;
    font-size: 32px;
    color: var(--ink-dark);
  }
  .card--back .wordmark__dot { background: var(--ink-dark); }

  .contact {
    position: absolute;
    left: 120px;
    bottom: 60px;
  }
  .contact__name {
    font-size: 30px;
    font-weight: 400;
    color: var(--accent);
    letter-spacing: 0.5px;
    line-height: 1.05;
  }
  .contact__role {
    font-size: 21px;
    color: var(--ink-grey);
    margin-bottom: 18px;
  }
  .contact__list { list-style: none; }
  .contact__item {
    display: flex;
    align-items: center;
    gap: 12px;
    font-size: 21px;
    color: var(--ink-grey);
    line-height: 1.45;
  }
  .contact__icon {
    width: 20px;
    height: 20px;
    flex: none;
    fill: var(--accent);
  }
</style>
</head>
<body>
<main class="sheet">
  <section class="card card--front" aria-label="Card front">
    <div class="emboss-disc" aria-hidden="true"></div>
    <div class="wordmark">
      <span class="wordmark__name">Ridgeline Electrical</span>
    </div>
  </section>

  <section class="card card--back" aria-label="Card back">
    <div class="wordmark">
      <span class="wordmark__dot"></span>
      <span class="wordmark__name">Ridgeline Electrical</span>
    </div>

    <div class="contact">
      <h1 class="contact__name">MARK ELLISON</h1>
      <p class="contact__role">Partner</p>
      <ul class="contact__list">
        <li class="contact__item">
          <svg class="contact__icon" viewBox="0 0 24 24" aria-hidden="true"><path d="M6.6 10.8a15.1 15.1 0 0 0 6.6 6.6l2.2-2.2a1 1 0 0 1 1-.25 11.4 11.4 0 0 0 3.6.57 1 1 0 0 1 1 1V20a1 1 0 0 1-1 1A17 17 0 0 1 3 4a1 1 0 0 1 1-1h3.5a1 1 0 0 1 1 1c0 1.25.2 2.45.57 3.57a1 1 0 0 1-.25 1z"/></svg>
          <span>443-555-0187</span>
        </li>
        <li class="contact__item">
          <svg class="contact__icon" viewBox="0 0 24 24" aria-hidden="true"><path d="M2 5h20v14H2z M3.5 6.5 12 13l8.5-6.5" fill="none" stroke="#2a8fd6" stroke-width="2"/></svg>
          <span>Mark@ridgelineelectrical.com</span>
        </li>
        <li class="contact__item">
          <svg class="contact__icon" viewBox="0 0 24 24" aria-hidden="true"><circle cx="12" cy="12" r="10"/><path d="M2 12h20M12 2c3 3 3 17 0 20M12 2c-3 3-3 17 0 20" fill="none" stroke="#fff" stroke-width="1.4"/></svg>
          <span>www.ridgelineelectrical.com</span>
        </li>
      </ul>
    </div>
  </section>
</main>
</body>
</html>
```